Workplace Safety Consultancy Business needs business card design

We need a business card for a new business providing workplace health and safety consulting called 'Worksure Guard'. We will be providing small to medium sized businesses assistance with OH&S and HR matters to ensure that their employees and the public are safe in the workplace and that they are meeting their legislative requirements. Would like to see the words 'practical workplace safety solutions' on the card. Personal details on the back. It needs to be clean, smart and professional (no fluff). Would like to see a simple logo if possible as well. Have been looking at orange and black, but open to other ideas.
Updates
Thank you to those to have created designs for us so far! We are really impressed with the impact of the black and orange having now seen it. Would be great if any further designs used those colours. Cheers.

Thank you to everyone that submitted a design. Your work is of the highest quality and we had a hard decision deciding. Sorry if we didn't choose your design, but it just came down to the one that stood out to us personally. Cheers.

Target Market(s)
Small-Medium business owners in Queensland, Australia. Age 25-60 male and female. Initially targeting those in the trade type industries
Industry/Entity Type
Health
Look and feel
Each slider illustrates characteristics of the customer's brand and the style your logo design should communicate.

```html
<!DOCTYPE html>
<html lang="en">
<head>
<meta charset="utf-8">
<title>Worksure Guard – Business Card</title>
<link rel="stylesheet" href="https://fonts.googleapis.com/css2?family=Exo+2:wght@500;600&family=Open+Sans:wght@400;600&display=swap">
<style>
  :root {
    --backdrop: #3a322d;
    --card: #1b1b1b;
    --card-tile: #202020;
    --orange: #f7a21b;
    --text-light: #e6e6e6;
    --text-dark: #1b1b1b;
  }
  html, body {
    margin: 0;
    width: 1200px;
    height: 716px;
    overflow: hidden;
    background: var(--backdrop);
  }
  .canvas {
    position: relative;
    width: 1200px;
    height: 716px;
  }
  .card {
    position: absolute;
    top: 213px;
    width: 500px;
    height: 290px;
    background: var(--card);
    overflow: hidden;
    box-shadow: 0 10px 30px rgba(0,0,0,.45);
  }
  .card-back { left: 60px; }
  .card-front { left: 640px; }

  .tile {
    position: absolute;
    background: var(--card-tile);
  }

  /* Back: contact side */
  .brand-band {
    position: absolute;
    left: 0; top: 0;
    width: 92px; height: 100%;
    background: var(--orange);
    display: flex;
    align-items: center;
    justify-content: center;
  }
  .brand-band .brand-name {
    writing-mode: vertical-rl;
    transform: rotate(180deg);
    font-family: "Exo 2", sans-serif;
    font-weight: 600;
    font-size: 25px;
    letter-spacing: 1px;
    color: var(--text-dark);
    white-space: nowrap;
  }
  .contact {
    position: absolute;
    left: 180px;
    top: 92px;
  }
  .contact-name {
    margin: 0 0 14px;
    font-family: "Open Sans", sans-serif;
    font-weight: 600;
    font-size: 14px;
    letter-spacing: .5px;
    text-transform: uppercase;
    color: var(--orange);
  }
  .contact-list {
    list-style: none;
    margin: 0; padding: 0;
    font-family: "Open Sans", sans-serif;
    font-size: 12px;
    color: var(--text-light);
  }
  .contact-list li {
    display: flex;
    align-items: center;
    gap: 9px;
    height: 19px;
  }
  .contact-icon {
    width: 12px; height: 12px;
    flex: none;
  }

  /* Front: logo side */
  .front-lockup {
    position: absolute;
    left: 0;
    right: 22px;
    top: 168px;
    display: flex;
    align-items: flex-start;
  }
  .accent-rule {
    flex: 1;
    height: 5px;
    margin-top: 20px;
    margin-right: 8px;
    background: var(--orange);
  }
  .front-brand {
    flex: none;
  }
  .front-brand .brand-name {
    display: block;
    font-family: "Exo 2", sans-serif;
    font-weight: 600;
    font-size: 28px;
    line-height: 1;
    letter-spacing: .5px;
    color: var(--orange);
    white-space: nowrap;
  }
  .tagline {
    display: block;
    margin-top: 8px;
    font-family: "Open Sans", sans-serif;
    font-size: 13px;
    color: var(--text-light);
    white-space: nowrap;
  }
  .tagline .highlight { color: var(--orange); }
</style>
</head>
<body>
<main class="canvas">

  <section class="card card-back" aria-label="Contact side">
    <div class="tile" style="left:200px;top:0;width:170px;height:70px"></div>
    <div class="tile" style="left:330px;top:170px;width:170px;height:120px"></div>
    <div class="tile" style="left:110px;top:200px;width:120px;height:90px"></div>

    <div class="brand-band">
      <span class="brand-name">WORKSURE GUARD</span>
    </div>

    <div class="contact">
      <h1 class="contact-name">Daniel Whitford</h1>
      <ul class="contact-list">
        <li>
          <svg class="contact-icon" viewBox="0 0 12 12" aria-hidden="true">
            <rect width="12" height="12" rx="1.5" fill="#f7a21b"/>
            <path d="M3.5 2.5h1.6l.7 2-1 .7a5 5 0 0 0 2 2l.7-1 2 .7v1.6a1 1 0 0 1-1 1A6.5 6.5 0 0 1 2.5 3.5a1 1 0 0 1 1-1z" fill="#1b1b1b"/>
          </svg>
          0412 555 038
        </li>
        <li>
          <svg class="contact-icon" viewBox="0 0 12 12" aria-hidden="true">
            <rect width="12" height="12" rx="1.5" fill="#f7a21b"/>
            <rect x="2.5" y="3.5" width="7" height="5" fill="none" stroke="#1b1b1b" stroke-width="1"/>
            <path d="M2.5 3.5 6 6.5l3.5-3" fill="none" stroke="#1b1b1b" stroke-width="1"/>
          </svg>
          daniel@worksureguard.net.au
        </li>
        <li>
          <svg class="contact-icon" viewBox="0 0 12 12" aria-hidden="true">
            <rect width="12" height="12" rx="1.5" fill="#f7a21b"/>
            <circle cx="6" cy="6" r="3.5" fill="none" stroke="#1b1b1b" stroke-width="1"/>
            <path d="M2.5 6h7M6 2.5c-1.6 2-1.6 5 0 7M6 2.5c1.6 2 1.6 5 0 7" fill="none" stroke="#1b1b1b" stroke-width=".8"/>
          </svg>
          www.worksureguard.net.au
        </li>
      </ul>
    </div>
  </section>

  <section class="card card-front" aria-label="Logo side">
    <div class="tile" style="left:70px;top:30px;width:150px;height:110px"></div>
    <div class="tile" style="left:250px;top:0;width:140px;height:90px"></div>
    <div class="tile" style="left:360px;top:110px;width:140px;height:180px"></div>

    <div class="front-lockup">
      <div class="accent-rule"></div>
      <div class="front-brand">
        <span class="brand-name">WORKSURE GUARD</span>
        <span class="tagline">practical workplace <span class="highlight">safety</span> solutions</span>
      </div>
    </div>
  </section>

</main>
</body>
</html>
```